Medical Device Company needs website

We are a start-up medical device company looking to sell boot (foot) and brace (ankle) products on Shopify. We are still working on the name but you can use Kaltir as a placeholder- no logo yet)

Website information:
- Look: modern/tech with clean lines and symmetry.
- Colors: teal, white, black, and greys.
- Headers: home, shop, about us, help, blog
- Icons (upper right): search, my account and shopping cart
-place to sign up for newsletter

```html
<!DOCTYPE html>
<html lang="en">
<head>
<meta charset="utf-8">
<title>Kaltir — Boots &amp; Braces</title>
<link href="https://fonts.googleapis.com/css2?family=Oswald:wght@400;500;600;700&family=Jost:wght@400;500;600&display=swap" rel="stylesheet">
<style>
:root{
  --teal:#10a39b;
  --teal-light:#14b8ad;
  --ink:#121212;
  --black:#0c0c0c;
  --grey:#efefef;
  --grey-mid:#d9d9d9;
  --text:#333;
  --white:#fff;
}
*{box-sizing:border-box;margin:0;padding:0}
html,body{width:1200px;height:4193px;overflow:hidden}
body{position:relative;background:var(--white);font-family:"Jost",sans-serif;color:var(--text)}
.abs{position:absolute}
.display{font-family:"Oswald",sans-serif;text-transform:uppercase;color:var(--ink);letter-spacing:.14em;font-weight:500}
.eyebrow{font-size:11px;letter-spacing:.14em;color:var(--teal);text-transform:uppercase;text-align:center;width:1200px;left:0}
.section-title{width:1200px;left:0;text-align:center;font-size:28px;line-height:36px}
.link-arrow{font-family:"Oswald",sans-serif;font-size:11px;letter-spacing:.22em;color:var(--teal);text-transform:uppercase;font-weight:500;white-space:nowrap}
.photo{position:absolute}

/* header */
.hero-bg{left:0;top:0;width:1200px;height:676px;background:linear-gradient(135deg,#2a2f33 0%,#161a1c 55%,#0f1112 100%)}
.logo{left:163px;top:22px;font-family:"Oswald",sans-serif;font-weight:700;font-size:30px;line-height:38px;letter-spacing:.06em;color:var(--white);text-transform:uppercase}
.search{left:793px;top:15px;width:127px;height:27px;background:#1b1b1b;border:1px solid #333;color:#999;font-size:10px;padding:6px 10px}
.search svg{position:absolute;right:8px;top:6px}
.header-icons{left:975px;top:16px}
.nav{top:64px;font-size:10px;color:var(--white);letter-spacing:.05em;font-weight:500;white-space:nowrap}

.hero-title{left:193px;top:330px;font-family:"Oswald",sans-serif;font-size:48px;line-height:54px;color:var(--white);letter-spacing:.12em;text-transform:uppercase;font-weight:500;white-space:nowrap}
.hero-copy{left:196px;top:456px;width:300px;font-size:11px;line-height:16px;color:#e8fbf9}

/* product cards */
.card{position:absolute;top:778px;width:207px;height:280px;background:var(--white);box-shadow:0 10px 40px rgba(0,0,0,.08);text-align:center}
.card .shot{position:absolute;left:50px;top:18px;width:107px;height:130px;border-radius:6px}
.card h3{position:absolute;top:178px;width:100%;font-family:"Oswald",sans-serif;font-weight:500;font-size:13px;letter-spacing:.06em;color:var(--ink)}
.card p{position:absolute;top:199px;width:100%;font-size:9px;line-height:11px;color:#555}
.btn{display:inline-block;background:var(--teal);color:var(--white);font-family:"Oswald",sans-serif;font-size:8px;letter-spacing:.12em;text-transform:uppercase;text-align:center}
.card .btn{position:absolute;left:62px;top:236px;width:82px;height:21px;line-height:21px}

/* welcome */
.welcome-copy{left:163px;width:375px;font-size:11.5px;line-height:19px;color:#333}

/* best sellers */
.seller{position:absolute;top:1897px;width:257px;height:276px}
.seller .shot{position:absolute;left:78px;top:8px;width:100px;height:138px;border-radius:6px}
.seller h3{position:absolute;top:168px;width:100%;text-align:center;font-family:"Oswald",sans-serif;font-weight:500;font-size:13.5px;line-height:18px;letter-spacing:.07em;color:var(--white)}
.seller .price{position:absolute;top:211px;width:100%;text-align:center;font-size:12px;color:var(--white)}

/* contact */
.field{position:absolute;left:597px;width:367px;border-bottom:1px solid #bdbdbd;font-size:11px;color:#444}

/* blog */
.post{position:absolute;top:3142px;width:417px}
.post .shot{width:417px;height:239px}
.post .date{margin:30px 0 0 6px;font-size:10px;letter-spacing:.1em;color:#222}
.post h3{margin:6px 0 0 6px;font-family:"Oswald",sans-serif;font-weight:500;font-size:14px;letter-spacing:.05em;color:var(--ink)}
.post p{margin:6px 0 0 6px;width:370px;font-size:10.5px;line-height:18px;color:#333}
.post .btn{margin:10px 0 0 9px;width:83px;height:22px;line-height:22px}

/* footer */
.foot-col{position:absolute;top:3980px}
.foot-col h4{font-family:"Oswald",sans-serif;font-weight:400;font-size:12px;letter-spacing:.06em;color:var(--teal);margin-bottom:8px}
.foot-col a{display:block;font-size:9px;line-height:18.5px;color:var(--white);text-decoration:none;text-transform:uppercase;white-space:nowrap}
</style>
</head>
<body>

<!-- HEADER + HERO -->
<div class="abs hero-bg" role="img" aria-label="Photo of two runners sprinting through a dark parking garage"></div>
<svg class="abs" style="left:0;top:500px" width="1200" height="180"><polygon points="0,8 1200,176 1200,180 0,180" fill="#fff"/></svg>
<div class="abs logo">Kaltir</div>
<div class="abs search">Search
  <svg width="13" height="13" viewBox="0 0 13 13" fill="none" stroke="#fff" stroke-width="1.6"><circle cx="5.5" cy="5.5" r="4"/><line x1="8.5" y1="8.5" x2="12" y2="12"/></svg>
</div>
<svg class="abs header-icons" width="65" height="22" viewBox="0 0 65 22" fill="none" stroke="#fff" stroke-width="1.5">
  <circle cx="13" cy="8" r="4"/><path d="M5 19c1-4 4-6 8-6s7 2 8 6"/>
  <path d="M42 3h4l3 11h11l2-8H47"/><circle cx="50" cy="18" r="1.5"/><circle cx="58" cy="18" r="1.5"/>
</svg>
<nav>
  <span class="abs nav" style="left:563px">HOME</span>
  <span class="abs nav" style="left:679px">SHOP</span>
  <span class="abs nav" style="left:786px">ABOUT US</span>
  <span class="abs nav" style="left:915px">HELP</span>
  <span class="abs nav" style="left:1011px">BLOG</span>
</nav>

<svg class="abs" style="left:160px;top:249px" width="405" height="405">
  <defs><linearGradient id="heroTeal" x1="0" y1="0" x2="1" y2="1"><stop offset="0" stop-color="#14bcb1"/><stop offset="1" stop-color="#0a8a83"/></linearGradient></defs>
  <polygon points="0,0 340,0 402,337 0,402" fill="url(#heroTeal)"/>
</svg>
<h1 class="abs hero-title">Challenge<br>your limits</h1>
<p class="abs hero-copy">Duis aute irure dolor in reprehenderit in voluptate velit esse cillum dolore eu fugiat nulla pariatur.</p>
<span class="abs link-arrow" style="left:197px;top:514px;color:#fff">Continue reading &nbsp;›</span>

<!-- ESSENTIALS -->
<p class="abs eyebrow" style="top:702px">Lorem ipsum dolor sit amet</p>
<h2 class="abs display section-title" style="top:718px">Essential for everybody</h2>

<div class="card" style="left:163px">
  <div class="shot" role="img" aria-label="White and grey walking boot" style="background:linear-gradient(160deg,#e8eaee,#b9c0c8)"></div>
  <h3>CONGUE EGESTAS FAMES</h3><p>Metus dapibus suscipit dapibus<br>Maximus pellentesque</p>
  <span class="btn">Add to cart</span>
</div>
<div class="card" style="left:386px">
  <div class="shot" role="img" aria-label="Black strapped walking boot" style="background:linear-gradient(160deg,#4a4a4a,#161616)"></div>
  <h3>CONGUE EGESTAS FAMES</h3><p>Metus dapibus suscipit dapibus<br>Maximus pellentesque</p>
  <span class="btn">Add to cart</span>
</div>
<div class="card" style="left:609px">
  <div class="shot" role="img" aria-label="Black ankle compression sleeve on a foot" style="background:linear-gradient(160deg,#d9a07c,#1d1d1d)"></div>
  <h3>CONGUE EGESTAS FAMES</h3><p>Metus dapibus suscipit dapibus<br>Maximus pellentesque</p>
  <span class="btn">Add to cart</span>
</div>
<div class="card" style="left:832px">
  <div class="shot" role="img" aria-label="White air walker boot with teal accents" style="background:linear-gradient(160deg,#eef0f2,#aab4bd)"></div>
  <h3>CONGUE EGESTAS FAMES</h3><p>Metus dapibus suscipit dapibus<br>Maximus pellentesque</p>
  <span class="btn">Add to cart</span>
</div>
<svg class="abs" style="left:1055px;top:908px" width="12" height="18" fill="none" stroke="#222" stroke-width="2"><polyline points="2,2 9,9 2,16"/></svg>

<!-- WELCOME -->
<svg class="abs" style="left:0;top:1151px" width="810" height="565"><polygon points="0,0 809,0 667,563 0,495" fill="#efefef"/></svg>
<div class="photo" role="img" aria-label="Photo of a man walking on crutches with a boot in a bright clinic room" style="left:596px;top:1195px;width:604px;height:467px;clip-path:polygon(115px 0,604px 0,604px 467px,0 467px);background:linear-gradient(135deg,#f2f0ec 0%,#d8d3cb 60%,#b8b0a4 100%)"></div>
<p class="abs" style="left:161px;top:1230px;font-size:10px;letter-spacing:.14em;color:#444">LOREM IPSUM DOLOR SIT</p>
<p class="abs display" style="left:161px;top:1244px;font-size:30px;line-height:36px;letter-spacing:.12em">Welcome to</p>
<p class="abs display" style="left:161px;top:1272px;font-size:72px;line-height:80px;letter-spacing:.12em;font-weight:500">Kaltir</p>
<p class="abs welcome-copy" style="top:1368px">Sit congue egestas fames vehicula suscipit arcu sapien. Tincidunt aliquet risus scelerisque fermentum luctus; maecenas praesent sociosqu eu. Hendrerit aliquam hendrerit ultricies facilisis eleifend arcu netus convallis. Mauris tincidunt sapien vulputate suspendisse maximus varius habitasse.</p>
<p class="abs welcome-copy" style="top:1481px">Maximus himenaeos vestibulum purus aliquam placerat parturient. Senectus tempor commodo ex sagittis sociosqu.</p>
<span class="abs link-arrow" style="left:165px;top:1548px">Continue reading &nbsp;›</span>

<!-- BEST SELLERS -->
<p class="abs eyebrow" style="top:1795px">Lorem ipsum dolor sit amet</p>
<h2 class="abs display section-title" style="top:1811px">Best selling products</h2>

<div class="seller" style="left:161px">
  <svg class="abs" width="257" height="276"><polygon points="0,0 257,0 257,276 0,236" fill="#121212"/><rect x="197" y="226" width="60" height="50" fill="#10a39b"/><path d="M214 251h26M232 243l8 8-8 8" stroke="#fff" stroke-width="1.6" fill="none"/></svg>
  <div class="shot" role="img" aria-label="Black tall walking boot" style="background:linear-gradient(160deg,#555,#1a1a1a)"></div>
  <h3>LOREM IPSUM ODOR AMET<br>VEHICULA SUSCIPIT</h3><p class="price">$120.00</p>
</div>
<div class="seller" style="left:467px">
  <svg class="abs" width="257" height="276"><polygon points="0,0 257,0 257,276 0,236" fill="#121212"/><rect x="197" y="226" width="60" height="50" fill="#10a39b"/><path d="M214 251h26M232 243l8 8-8 8" stroke="#fff" stroke-width="1.6" fill="none"/></svg>
  <div class="shot" role="img" aria-label="White walking boot with teal sole" style="background:linear-gradient(160deg,#e9ecef,#8d99a3)"></div>
  <h3>LOREM IPSUM ODOR AMET<br>VEHICULA SUSCIPIT</h3><p class="price">$120.00</p>
</div>
<div class="seller" style="left:772px">
  <svg class="abs" width="257" height="276"><polygon points="0,0 257,0 257,276 0,236" fill="#121212"/><rect x="197" y="226" width="60" height="50" fill="#10a39b"/><path d="M214 251h26M232 243l8 8-8 8" stroke="#fff" stroke-width="1.6" fill="none"/></svg>
  <div class="shot" role="img" aria-label="Grey and black air walker boot" style="background:linear-gradient(160deg,#9aa3ab,#2b2f33)"></div>
  <h3>LOREM IPSUM ODOR AMET<br>VEHICULA SUSCIPIT</h3><p class="price">$120.00</p>
</div>
<svg class="abs" style="left:1040px;top:2036px" width="12" height="18" fill="none" stroke="#222" stroke-width="2"><polyline points="2,2 9,9 2,16"/></svg>

<!-- PERFECT SHAPE -->
<svg class="abs" style="left:0;top:2270px" width="1200" height="1335"><polygon points="0,160 1200,0 1200,1335 0,1335" fill="#efefef"/></svg>
<div class="photo" role="img" aria-label="Photo of a smiling man in a boot seated on a grey sofa with crutches, on a beige rug" style="left:106px;top:2230px;width:627px;height:367px;border-radius:40px 40px 50% 50% / 30px 30px 20px 20px;background:linear-gradient(180deg,rgba(0,0,0,0) 0%,#8d8d8d 40%,#6d6d6d 70%,#cdbfae 85%,#e2d7c9 100%)"></div>
<h2 class="abs display" style="left:736px;top:2318px;font-size:28px;line-height:36px;white-space:nowrap">The perfect shape</h2>
<p class="abs" style="left:736px;top:2372px;width:280px;font-size:11px;line-height:18px;color:#333">Sit congue egestas fames vehicula suscipit arcu sapien. Tincidunt aliquet risus scelerisque.</p>
<span class="abs link-arrow" style="left:736px;top:2424px">Shop now &nbsp;›</span>

<!-- CONTACT -->
<h2 class="abs display" style="left:166px;top:2684px;font-size:46px;line-height:50px;letter-spacing:.16em">Help me<br>now</h2>
<svg class="abs" style="left:167px;top:2818px" width="18" height="18" viewBox="0 0 24 24" fill="#222"><path d="M6.6 10.8a15 15 0 0 0 6.6 6.6l2.2-2.2a1 1 0 0 1 1-.25 11.4 11.4 0 0 0 3.6.57 1 1 0 0 1 1 1V20a1 1 0 0 1-1 1A17 17 0 0 1 3 4a1 1 0 0 1 1-1h3.5a1 1 0 0 1 1 1c0 1.25.2 2.45.57 3.6a1 1 0 0 1-.25 1z"/></svg>
<p class="abs" style="left:197px;top:2813px;font-size:20px;line-height:26px;color:#1a1a1a;white-space:nowrap">+1 555 014 2738</p>
<svg class="abs" style="left:168px;top:2861px" width="18" height="13" viewBox="0 0 18 13"><rect width="18" height="13" fill="#222"/><path d="M1 1l8 6 8-6" stroke="#efefef" stroke-width="1.2" fill="none"/></svg>
<p class="abs" style="left:197px;top:2851px;font-size:20px;line-height:26px;color:#1a1a1a;white-space:nowrap">support@kaltir.com</p>

<div class="field" style="top:2696px;height:20px">Name</div>
<div class="field" style="top:2728px;height:27px">Phone</div>
<div class="field" style="top:2768px;height:27px">Email</div>
<div class="field" style="top:2809px;height:77px">Message</div>
<span class="abs btn" style="left:599px;top:2904px;width:161px;height:41px;line-height:41px;font-size:11px">Submit</span>

<!-- BLOG -->
<h2 class="abs display section-title" style="top:3068px">Latest blog</h2>
<article class="post" style="left:169px">
  <div class="shot" role="img" aria-label="Photo of a person on crutches wearing an ankle brace and a sneaker" style="background:linear-gradient(135deg,#efe9e1,#c6b9a9 55%,#7c2530 100%)"></div>
  <p class="date">18 OCT 2024</p>
  <h3>LOREM IPSUM ODOR AMET, CONSECTETUER</h3>
  <p>Hendrerit aliquam hendrerit ultricies facilisis eleifend arcu netus convallis. Mauris tincidunt sapien vulputate suspendisse maximus varius habitasse.</p>
  <span class="btn">Read more</span>
</article>
<article class="post" style="left:619px">
  <div class="shot" role="img" aria-label="Close-up photo of a black ankle support with green straps" style="background:linear-gradient(135deg,#3a3a3a,#1b1b1b 55%,#c49a82 100%)"></div>
  <p class="date">18 OCT 2024</p>
  <h3>LOREM IPSUM ODOR AMET, CONSECTETUER</h3>
  <p>Hendrerit aliquam hendrerit ultricies facilisis eleifend arcu netus convallis. Mauris tincidunt sapien vulputate suspendisse maximus varius habitasse.</p>
  <span class="btn">Read more</span>
</article>

<!-- NEWSLETTER + FOOTER -->
<svg class="abs" style="left:0;top:3596px" width="1200" height="597"><polygon points="0,0 1200,108 1200,597 0,597" fill="#0c0c0c"/></svg>
<h2 class="abs display" style="left:166px;top:3720px;font-size:28px;line-height:36px;color:#fff;white-space:nowrap">Join our newsletter</h2>
<p class="abs" style="left:166px;top:3770px;width:330px;font-size:11px;line-height:18px;color:#ddd">Sit congue egestas fames vehicula suscipit arcu sapien. Tincidunt aliquet risus scelerisque.</p>
<div class="abs" style="left:164px;top:3816px;width:398px;height:46px;background:#1e1e1e;border:1px solid #2c2c2c"></div>
<span class="abs" style="left:179px;top:3832px;font-size:10.5px;color:#aaa">Enter Your Email Address</span>
<span class="abs link-arrow" style="left:446px;top:3832px;font-size:10px;letter-spacing:.06em">Subscribe now &nbsp;›</span>

<svg class="abs" style="left:778px;top:3632px" width="244" height="246"><polygon points="15,44 244,0 244,246 0,246" fill="#10a39b"/></svg>
<p class="abs" style="left:778px;top:3706px;width:244px;text-align:center;font-family:'Oswald',sans-serif;font-weight:700;font-size:30px;line-height:38px;letter-spacing:.06em;color:#fff;text-transform:uppercase">Kaltir</p>
<p class="abs" style="left:838px;top:3764px;width:140px;font-size:11px;line-height:16px;color:#e4fbf8">Quisque ipsum aliquet dignissim etiama</p>
<svg class="abs" style="left:842px;top:3817px" width="146" height="32" fill="none" stroke="#fff" stroke-width="1.6">
  <circle cx="16" cy="16" r="13"/><circle cx="53" cy="16" r="13"/><circle cx="91" cy="16" r="13"/><circle cx="128" cy="16" r="13"/>
</svg>

<div class="foot-col" style="left:169px"><h4>NAVIGATION</h4><a>Home</a><a>Shop</a><a>About us</a><a>Help</a><a>Blog</a></div>
<div class="foot-col" style="left:327px"><h4>ACCOUNT</h4><a>Sign up</a><a>Sign in</a><a>My account</a></div>
<div class="foot-col" style="left:470px"><h4>ORDER</h4><a>My cart</a><a>Return</a><a>Refund</a><a>Track order</a></div>
<div class="foot-col" style="left:612px"><h4>POLICY</h4><a>Privacy policy</a><a>Term and condition</a></div>
<div class="foot-col" style="left:799px"><h4>CONTACT US</h4><a>+1 555 014 2738</a><a style="text-transform:none">support@kaltir.com</a></div>
<p class="abs" style="left:0;top:4154px;width:1200px;text-align:center;font-size:9px;color:#888">© 2024 All Rights Reserved</p>

</body>
</html>
```